Falcrest security business card

Looking for a business card for my security company

Target Market(s)

Security

Industry/Entity Type

Security

Contact Information for Business Card

Name - Gil Marston. Title - General manager - direct 314 862.4490 website www. falcrestsecurityservices.example email - gil@ falcrestsecurityservices.example

Requirements
Must have
• Logo attached

```html
<!DOCTYPE html>
<html lang="en">
<head>
<meta charset="UTF-8">
<title>Falcrest Security Services – Business Card</title>
<link href="https://fonts.googleapis.com/css2?family=Montserrat:wght@500;800&family=Open+Sans:wght@400&display=swap" rel="stylesheet">
<style>
  :root {
    --backdrop: #2b2c2e;
    --card-black: #141414;
    --card-white: #ffffff;
    --gold: #c9a24a;
    --gold-edge: #a9853a;
    --ink: #111111;
  }
  * { margin: 0; padding: 0; box-sizing: border-box; }
  html, body {
    width: 1200px;
    height: 801px;
    overflow: hidden;
    background: var(--backdrop);
  }
  .stage {
    position: relative;
    width: 1200px;
    height: 801px;
    display: flex;
    align-items: center;
    justify-content: center;
    gap: 56px;
  }
  .card {
    position: relative;
    width: 525px;
    height: 300px;
    border-radius: 16px;
    border: 2px solid var(--gold-edge);
    overflow: hidden;
  }
  .card--front { background: var(--card-black); }
  .card--back { background: var(--card-white); }

  .brand {
    display: flex;
    align-items: center;
    gap: 12px;
    font-family: "Montserrat", sans-serif;
    font-weight: 800;
    text-transform: uppercase;
    letter-spacing: 1px;
    line-height: 1;
  }
  .brand__mark {
    width: 16px;
    height: 16px;
    flex: none;
  }
  .card--front .brand {
    position: absolute;
    left: 50%;
    top: 50%;
    transform: translate(-50%, -50%);
    font-size: 52px;
    color: var(--gold);
  }
  .card--front .brand__mark { background: var(--gold); }

  .card--back .brand {
    position: absolute;
    left: 50%;
    top: 58px;
    transform: translateX(-50%);
    font-size: 46px;
    color: var(--ink);
  }
  .card--back .brand__mark { background: var(--ink); }

  .person {
    position: absolute;
    left: 40px;
    bottom: 56px;
    color: var(--ink);
  }
  .person__name {
    font-family: "Montserrat", sans-serif;
    font-weight: 800;
    font-size: 24px;
    text-transform: uppercase;
    letter-spacing: 0.2px;
  }
  .person__title {
    font-family: "Montserrat", sans-serif;
    font-weight: 500;
    font-size: 14px;
    margin-top: 4px;
    letter-spacing: 0.4px;
  }

  .contact {
    position: absolute;
    right: 26px;
    bottom: 50px;
    list-style: none;
    font-family: "Open Sans", sans-serif;
    font-size: 12.5px;
    color: var(--ink);
  }
  .contact__item {
    display: flex;
    align-items: center;
    gap: 6px;
    margin-top: 5px;
  }
  .contact__icon { width: 11px; height: 11px; flex: none; fill: var(--ink); }
</style>
</head>
<body>
  <main class="stage">
    <section class="card card--front" aria-label="Business card front">
      <div class="brand"><span class="brand__mark"></span>Falcrest</div>
    </section>

    <section class="card card--back" aria-label="Business card back">
      <div class="brand"><span class="brand__mark"></span>Falcrest</div>

      <div class="person">
        <p class="person__name">Gil Marston</p>
        <p class="person__title">General manager</p>
      </div>

      <ul class="contact">
        <li class="contact__item">
          <svg class="contact__icon" viewBox="0 0 24 24" aria-hidden="true"><path d="M6.6 10.8a15.1 15.1 0 0 0 6.6 6.6l2.2-2.2a1 1 0 0 1 1-.25 11.4 11.4 0 0 0 3.6.57 1 1 0 0 1 1 1V20a1 1 0 0 1-1 1A17 17 0 0 1 3 4a1 1 0 0 1 1-1h3.5a1 1 0 0 1 1 1c0 1.25.2 2.45.57 3.57a1 1 0 0 1-.25 1z"/></svg>
          314 862.4490
        </li>
        <li class="contact__item">
          <svg class="contact__icon" viewBox="0 0 24 24" aria-hidden="true"><path d="M2 5h20v14H2z M2 5l10 8 10-8" fill="var(--ink)"/><path d="M3 6l9 7 9-7" fill="none" stroke="#fff" stroke-width="2"/></svg>
          gil@falcrestsecurityservices.example
        </li>
        <li class="contact__item">
          <svg class="contact__icon" viewBox="0 0 24 24" aria-hidden="true"><circle cx="12" cy="12" r="11"/><path d="M1 12h22M12 1c3 3.2 3 18.8 0 22M12 1c-3 3.2-3 18.8 0 22" fill="none" stroke="#fff" stroke-width="1.5"/></svg>
          www.falcrestsecurityservices.example
        </li>
      </ul>
    </section>
  </main>
</body>
</html>
```